Business Cards Needed for Innovative Healthcare Marketing Company

We are a marketing company focused on healthcare. Our company is all about rebranding yourself renewing your image and generating results. The phoenix stands for "reborn" or "rising" which we provide new brands for our clients we take their old brands and renew it with creativity and innovation. I am looking for a business card with color dimension. I have attached an example of a card I think has the look and feel of what I am trying to accomplish. I like that the card example has black and grey font colors, I like the font placement and the small logo, I really like the use of the colors on the right those are the colors of my logo. My logo is phoenix so maybe incorporating flames similar to that design. I would like the back a solid color maybe red with an opaque version of the logo and website. As a marketing company I am always open to creative liberty!

Target Market(s)

Doctors and business professionals.

Industry/Entity Type

Marketing

Contact Information for Business Card

Vornaly Health Care Marketing
Marnie Okonski- CEO
#(502)638-2947
email-marnie@vornaly.com
website- vornaly.com

Font styles to use
Sans Serif

Colors
ec1f27
f37122
ffc214
fbed22
fbf289
f04a50

Requirements
Must have
• The logo and required information
Nice to have
• icons by the information
Should not have
• child like font

```html
<!DOCTYPE html>
<html lang="en">
<head>
<meta charset="UTF-8">
<title>Vornaly Health Care Marketing – Business Cards</title>
<link href="https://fonts.googleapis.com/css2?family=Raleway:wght@300&family=Open+Sans:wght@400;600&display=swap" rel="stylesheet">
<style>
  :root {
    --bg: #ebe6de;
    --card: #ffffff;
    --brand-red: #d8262e;
    --orange-deep: #e0841c;
    --orange-mid: #f0a63a;
    --gold: #f2c230;
    --ink: #1d1d1d;
    --ink-soft: #3a3a3a;
    --swoosh-dark: #222222;
    --swoosh-grey: #9a9a9a;
  }
  * { margin: 0; padding: 0; box-sizing: border-box; }
  html, body { width: 1200px; height: 902px; overflow: hidden; }
  body { background: var(--bg); position: relative; font-family: "Open Sans", sans-serif; }

  .card {
    position: absolute;
    width: 540px;
    height: 310px;
    background: var(--card);
    box-shadow: 0 6px 18px rgba(0,0,0,0.18);
    overflow: hidden;
  }
  .card--back { left: 70px; top: 90px; }
  .card--front { left: 590px; top: 480px; }

  .brand {
    position: absolute;
    display: flex;
    align-items: center;
    gap: 16px;
    color: var(--brand-red);
    font-family: "Raleway", sans-serif;
    font-weight: 300;
  }
  .brand__mark {
    width: 54px; height: 54px;
    border-radius: 50%;
    background: var(--brand-red);
    flex: none;
  }
  .brand__text { display: flex; flex-direction: column; line-height: 1; }
  .brand__name { font-size: 52px; letter-spacing: 1px; }
  .brand__rule { height: 1px; background: var(--brand-red); margin: 8px 0 6px; }
  .brand__tag { font-size: 17px; letter-spacing: 1px; }

  .card--back .brand { left: 50%; top: 50%; transform: translate(-50%, -50%); }

  .card--front .brand { left: 200px; top: 40px; gap: 12px; }
  .card--front .brand__mark { width: 42px; height: 42px; }
  .card--front .brand__name { font-size: 40px; }
  .card--front .brand__tag { font-size: 13px; }

  .front-panel { position: absolute; inset: 0; }

  .holder {
    position: absolute;
    left: 30px; bottom: 26px;
    color: var(--ink-soft);
  }
  .holder__name { font-size: 21px; }
  .holder__role { font-size: 17px; margin-left: 22px; }

  .contacts {
    position: absolute;
    right: 24px; top: 160px;
    list-style: none;
    display: flex; flex-direction: column; align-items: flex-end; gap: 12px;
  }
  .contacts__item {
    display: flex; align-items: center; gap: 12px;
    font-size: 16px; font-weight: 600; color: var(--ink);
  }
  .contacts__icon {
    width: 16px; height: 16px;
    background: var(--orange-mid);
    border-radius: 2px;
    display: flex; align-items: center; justify-content: center;
  }
</style>
</head>
<body>

  <section class="card card--back" aria-label="Card back">
    <div class="brand">
      <span class="brand__mark"></span>
      <div class="brand__text">
        <span class="brand__name">VORNALY</span>
        <span class="brand__rule"></span>
        <span class="brand__tag">HEALTH CARE MARKETING</span>
      </div>
    </div>
  </section>

  <section class="card card--front" aria-label="Card front">
    <svg class="front-panel" width="540" height="310" viewBox="0 0 540 310">
      <defs>
        <linearGradient id="panelFill" x1="0" y1="0" x2="0.6" y2="1">
          <stop offset="0" stop-color="var(--orange-deep)"/>
          <stop offset="0.5" stop-color="var(--orange-mid)"/>
          <stop offset="1" stop-color="var(--gold)"/>
        </linearGradient>
      </defs>
      <path d="M0,0 H135 C160,120 260,240 350,310 H0 Z" fill="var(--swoosh-grey)"/>
      <path d="M0,0 H125 C150,125 250,240 340,310 H0 Z" fill="var(--swoosh-dark)"/>
      <path d="M0,0 H112 C138,128 235,240 322,310 H0 Z" fill="#ffffff"/>
      <path d="M0,0 H104 C130,130 225,240 312,310 H0 Z" fill="url(#panelFill)"/>
    </svg>

    <div class="brand">
      <span class="brand__mark"></span>
      <div class="brand__text">
        <span class="brand__name">VORNALY</span>
        <span class="brand__rule"></span>
        <span class="brand__tag">HEALTH CARE MARKETING</span>
      </div>
    </div>

    <div class="holder">
      <p class="holder__name">Marnie Okonski</p>
      <p class="holder__role">CEO</p>
    </div>

    <ul class="contacts">
      <li class="contacts__item">vornaly.com
        <span class="contacts__icon">
          <svg width="10" height="10" viewBox="0 0 10 10" fill="none" stroke="#fff" stroke-width="1">
            <circle cx="5" cy="5" r="4"/><path d="M1 5H9M5 1C3 3 3 7 5 9M5 1C7 3 7 7 5 9"/>
          </svg>
        </span>
      </li>
      <li class="contacts__item">#(502)638-2947
        <span class="contacts__icon">
          <svg width="10" height="10" viewBox="0 0 10 10">
            <path d="M2 1L4 1L4.6 3L3.4 4C4 5.4 4.8 6.2 6 6.6L7 5.4L9 6V8C9 8.6 8.6 9 8 9C4.5 9 1 5.5 1 2C1 1.4 1.4 1 2 1Z" fill="#fff"/>
          </svg>
        </span>
      </li>
      <li class="contacts__item">marnie@vornaly.com
        <span class="contacts__icon">
          <svg width="10" height="10" viewBox="0 0 10 10" fill="none" stroke="#fff" stroke-width="1">
            <rect x="1" y="2.5" width="8" height="5.5"/><path d="M1 2.5L5 5.5L9 2.5"/>
          </svg>
        </span>
      </li>
    </ul>
  </section>

</body>
</html>
```